Flyer for DK Siren Installers

This flyer will help our technicians upsell/educate our current customers on the different service packages that we offer when the tech is in the customers home.

```html
<!DOCTYPE html>
<html lang="en">
<head>
<meta charset="utf-8">
<title>DK Siren Installers – Package Flyers</title>
<link href="https://fonts.googleapis.com/css2?family=Roboto:wght@400;500;700&family=Roboto+Condensed:wght@700&display=swap" rel="stylesheet">
<style>
  :root {
    --navy: #2b3477;
    --green: #77b843;
    --panel: #eceef3;
    --ink: #5a5f6b;
    --backdrop: #e4e5e8;
    --white: #ffffff;
  }
  * { box-sizing: border-box; margin: 0; padding: 0; }
  html, body { width: 1200px; height: 817px; overflow: hidden; }
  body { background: var(--backdrop); font-family: "Roboto", Arial, sans-serif; position: relative; }

  .flyer {
    position: absolute; top: 93px; width: 493px; height: 638px;
    background: var(--white); box-shadow: 0 4px 14px rgba(0,0,0,.18); overflow: hidden;
  }
  .flyer--devices { left: 89px; }
  .flyer--plans { left: 625px; }

  .brand {
    position: absolute; left: 16px; top: 10px;
    font-weight: 700; font-size: 19px; color: var(--navy); letter-spacing: .4px;
  }
  .series-title {
    position: absolute; right: 15px; top: 11px;
    font-size: 14.5px; font-weight: 400; color: var(--navy);
  }
  .series-title em { font-style: normal; color: var(--green); }
  .header-band { position: absolute; left: 0; top: 33px; }

  .hero { position: absolute; left: 0; top: 42px; width: 493px; height: 223px; }
  .hero--house {
    background:
      radial-gradient(ellipse 60% 40% at 55% 80%, rgba(230,220,200,.55), transparent 70%),
      linear-gradient(180deg, #9aa2bf 0%, #7d839c 25%, #5d6272 50%, #6b6f78 72%, #bdb8ad 100%);
  }
  .hero--family {
    background:
      radial-gradient(ellipse 45% 55% at 72% 40%, rgba(40,55,95,.55), transparent 70%),
      radial-gradient(ellipse 40% 45% at 50% 35%, rgba(205,170,130,.6), transparent 70%),
      linear-gradient(180deg, #a8956a 0%, #6f7f48 45%, #4e6b33 75%, #86a35a 100%);
  }
  .hero-badges { position: absolute; left: 0; top: 42px; }
  .hero-band { position: absolute; left: 0; top: 265px; }

  .tagline {
    position: absolute; left: 19px; top: 67px; width: 130px; height: 130px;
    display: flex; align-items: center; justify-content: center; text-align: center;
  }
  .tagline svg { position: absolute; inset: 0; }
  .tagline span {
    position: relative; color: var(--white); font-size: 17px; line-height: 1.25; font-weight: 400;
  }

  .packages {
    position: absolute; left: 15px; top: 291px; width: 465px; height: 292px;
    display: grid; gap: 5px;
  }
  .flyer--devices .packages { grid-template-columns: repeat(3, 1fr); }
  .flyer--plans .packages { grid-template-columns: repeat(4, 1fr); }
  .package-col { background: var(--panel); padding: 12px 6px 0; display: flex; flex-direction: column; }
  .flyer--devices .package-col { gap: 10px; }

  .package-card {
    border: 1.5px solid var(--navy); border-radius: 4px; overflow: hidden; background: var(--white);
  }
  .package-photo { height: 67px; }
  .package-photo--tall { height: 98px; }
  .photo--doorbell { background: radial-gradient(ellipse 55% 60% at 50% 55%, #8c8f96, #d6d8dd 55%, #f7f7f9 90%); }
  .photo--thermostat { background: radial-gradient(ellipse 45% 55% at 50% 50%, #e2e4e8, #f0f1f3 60%, #fafafb); }
  .photo--deadbolt { background: radial-gradient(ellipse 55% 50% at 50% 45%, #c9a94a, #b9b8b2 45%, #f5f5f6 90%); }
  .photo--garage { background: radial-gradient(ellipse 45% 45% at 50% 50%, #3a3b40, #8a8c92 60%, #f5f5f6 95%); }
  .photo--indoor { background: radial-gradient(ellipse 35% 50% at 50% 45%, #55585f, #c9cbd0 55%, #f7f7f9 90%); }
  .photo--outdoor { background: radial-gradient(ellipse 45% 40% at 50% 50%, #7a7d84, #d2d4d8 55%, #f7f7f9 90%); }
  .photo--board { background: radial-gradient(ellipse 40% 40% at 45% 60%, #4f7a52, #aab4ac 55%, #f5f5f6 90%); }
  .photo--panel { background: radial-gradient(ellipse 45% 40% at 50% 45%, #9aa7c2, #d9dce2 55%, #f7f7f9 90%); }

  .package-label {
    background: var(--navy); color: var(--white);
    font-size: 8.5px; font-weight: 500; text-align: center;
    height: 26px; display: flex; align-items: center; justify-content: center; padding: 0 3px; line-height: 1.3;
    white-space: nowrap;
  }
  .package-label--tall { height: 54px; }
  .package-note { font-size: 7px; line-height: 1.2; color: var(--ink); text-align: center; padding: 0 3px; margin-top: 4px; }
  .flyer--plans .package-note { margin-top: 14px; }
  .flyer--plans .package-note--fine { font-size: 6px; margin-top: 28px; }
  .flyer--plans .package-note--second { margin-top: 24px; }

  .footer { position: absolute; left: 0; top: 590px; width: 493px; height: 48px; }
  .footer-bg { position: absolute; inset: 0; }
  .footer-phone {
    position: absolute; left: 16px; top: 9px; display: flex; align-items: center; gap: 6px;
    font-family: "Roboto Condensed", Arial, sans-serif; font-weight: 700; font-size: 23px; color: var(--white);
  }
  .footer-links {
    position: absolute; left: 202px; top: 17px; display: flex; gap: 10px;
    font-size: 9.5px; color: var(--white);
  }
  .footer-links span { display: flex; align-items: center; gap: 4px; }
</style>
</head>
<body>

<section class="flyer flyer--devices">
  <div class="brand">DK SIREN INSTALLERS</div>
  <div class="series-title">DK <em>SIREN</em> PACKAGES</div>
  <svg class="header-band" width="493" height="9"><polygon points="185,0 493,0 493,9 176,9" fill="var(--green)"/></svg>

  <div class="hero hero--house" role="img" aria-label="Photo of a two-storey suburban house at dusk"></div>
  <svg class="hero-badges" width="493" height="223" aria-hidden="true">
    <g fill="var(--green)" opacity=".9">
      <polygon points="379,101 394,110 394,128 379,137 364,128 364,110"/>
      <polygon points="302,146 313,152 313,166 302,172 291,166 291,152"/>
      <polygon points="164,190 174,196 174,208 164,214 154,208 154,196"/>
      <polygon points="217,177 227,183 227,197 217,203 207,197 207,183"/>
      <polygon points="98,141 106,146 106,156 98,161 90,156 90,146"/>
      <polygon points="446,148 455,153 455,165 446,170 437,165 437,153"/>
    </g>
  </svg>
  <svg class="hero-band" width="493" height="10"><polygon points="0,0 310,0 300,10 0,10" fill="var(--green)"/></svg>

  <div class="packages">
    <div class="package-col">
      <div class="package-item">
        <div class="package-card">
          <div class="package-photo photo--doorbell" role="img" aria-label="Video doorbell cameras"></div>
          <div class="package-label">DOOR BELL CAMERAS</div>
        </div>
        <p class="package-note">One home automation device requires a $6 a month increase per device with a 60 month renewal</p>
      </div>
      <div class="package-item">
        <div class="package-card">
          <div class="package-photo photo--garage" role="img" aria-label="Garage door controller unit"></div>
          <div class="package-label">GARAGE CONTROLLER</div>
        </div>
        <p class="package-note">One home automation device requires a $6 a month increase per device with a 60 month renewal</p>
      </div>
    </div>
    <div class="package-col">
      <div class="package-item">
        <div class="package-card">
          <div class="package-photo photo--thermostat" role="img" aria-label="Smart wall thermostat"></div>
          <div class="package-label">HL THERMOSTAT</div>
        </div>
        <p class="package-note">One home automation device requires a $6 a month increase per device with a 60 month renewal</p>
      </div>
      <div class="package-item">
        <div class="package-card">
          <div class="package-photo photo--indoor" role="img" aria-label="Indoor security camera"></div>
          <div class="package-label">INDOOR CAMERA</div>
        </div>
        <p class="package-note">One home automation device requires a $6 a month increase per device with a 60 month renewal</p>
      </div>
    </div>
    <div class="package-col">
      <div class="package-item">
        <div class="package-card">
          <div class="package-photo photo--deadbolt" role="img" aria-label="Three smart deadbolt locks in different finishes"></div>
          <div class="package-label">AUTO DEADBOLT</div>
        </div>
        <p class="package-note">One home automation device requires a $6 a month increase per device with a 60 month renewal</p>
      </div>
      <div class="package-item">
        <div class="package-card">
          <div class="package-photo photo--outdoor" role="img" aria-label="Outdoor security cameras"></div>
          <div class="package-label">OUTDOOR CAMERAS</div>
        </div>
        <p class="package-note">Outdoor camera<br>Requires a $12 a month<br>Increase for the camera Per camera</p>
      </div>
    </div>
  </div>

  <div class="footer">
    <svg class="footer-bg" width="493" height="48">
      <polygon points="188,14 493,14 493,36 188,36" fill="var(--green)"/>
      <polygon points="0,36 493,36 493,48 0,48" fill="var(--navy)"/>
      <polygon points="0,0 182,0 196,36 200,48 0,48" fill="var(--navy)"/>
      <line x1="186" y1="0" x2="202" y2="40" stroke="var(--navy)" stroke-width="2"/>
    </svg>
    <div class="footer-phone">
      <svg width="20" height="22" viewBox="0 0 20 22"><rect x="5" y="1" width="11" height="20" rx="2" fill="none" stroke="#fff" stroke-width="2"/><path d="M1 6 Q4 3 5 6 L5 14 Q3 17 1 14 Z" fill="#fff"/></svg>
      555-014-2290
    </div>
    <div class="footer-links">
      <span><svg width="9" height="9"><circle cx="4.5" cy="4.5" r="4" fill="none" stroke="#fff" stroke-width="1.2"/></svg>info@dksireninstallers.com</span>
      <span><svg width="9" height="9"><circle cx="4.5" cy="4.5" r="4" fill="none" stroke="#fff" stroke-width="1.2"/><line x1=".5" y1="4.5" x2="8.5" y2="4.5" stroke="#fff"/></svg>www.dksireninstallers.com</span>
    </div>
  </div>
</section>

<section class="flyer flyer--plans">
  <div class="brand">DK SIREN INSTALLERS</div>
  <div class="series-title">DK <em>SIREN</em> PACKAGES</div>
  <svg class="header-band" width="493" height="9"><polygon points="185,0 493,0 493,9 176,9" fill="var(--green)"/></svg>

  <div class="hero hero--family" role="img" aria-label="Photo of a family playing with soap bubbles on a lawn"></div>
  <div class="tagline">
    <svg width="130" height="130" viewBox="0 0 130 130"><polygon points="65,0 130,33 130,97 65,130 0,97 0,33" fill="var(--green)" opacity=".92"/></svg>
    <span>PROTECT<br>WHAT’S<br>IPORTANT</span>
  </div>
  <svg class="hero-band" width="493" height="10"><polygon points="0,0 393,0 383,10 0,10" fill="var(--green)"/></svg>

  <div class="packages">
    <div class="package-col">
      <div class="package-card">
        <div class="package-photo package-photo--tall photo--doorbell" role="img" aria-label="Video doorbell and outdoor camera"></div>
        <div class="package-label package-label--tall">DOORBELL and<br>OUTDOOR CAMERA</div>
      </div>
      <p class="package-note">Doorbell camera and an outdoor camera requires a $20 increase a month for both these devices</p>
      <p class="package-note package-note--fine">**requirements: 60 month agreement renewal + $50 install fee per outdoor camera</p>
    </div>
    <div class="package-col">
      <div class="package-card">
        <div class="package-photo package-photo--tall photo--outdoor" role="img" aria-label="Set of outdoor cameras"></div>
        <div class="package-label package-label--tall" style="font-size:8px">2-4 OUTDOOR CAMERAS<br>+12 PER CAMERA</div>
      </div>
      <p class="package-note">Two or more outdoor cameras requires a $12 increase per month per outdoor camera</p>
      <p class="package-note package-note--fine">**Requirement: +$6 5-8 cameras due to more clips package</p>
    </div>
    <div class="package-col">
      <div class="package-card">
        <div class="package-photo package-photo--tall photo--board" role="img" aria-label="Cellular communicator board with wiring"></div>
        <div class="package-label package-label--tall">PHONELINE</div>
      </div>
      <p class="package-note">1st option: phoneline to cell primary no app requires $7 increase per month, also requires a 60 month renewal</p>
      <p class="package-note package-note--second">2nd option: phoneline to cell primary with app requires a $13 a month increase, also requires a 60 month renewal</p>
    </div>
    <div class="package-col">
      <div class="package-card">
        <div class="package-photo package-photo--tall photo--panel" role="img" aria-label="Security control panel with touchscreen"></div>
        <div class="package-label package-label--tall">HUB CONTROL</div>
      </div>
      <p class="package-note">Hub control 2 panel upgrade requires a $5 increase per month with a 60 month renewal and a one time fee $100</p>
    </div>
  </div>

  <div class="footer">
    <svg class="footer-bg" width="493" height="48">
      <polygon points="188,14 493,14 493,36 188,36" fill="var(--green)"/>
      <polygon points="0,36 493,36 493,48 0,48" fill="var(--navy)"/>
      <polygon points="0,0 182,0 196,36 200,48 0,48" fill="var(--navy)"/>
      <line x1="186" y1="0" x2="202" y2="40" stroke="var(--navy)" stroke-width="2"/>
    </svg>
    <div class="footer-phone">
      <svg width="20" height="22" viewBox="0 0 20 22"><rect x="5" y="1" width="11" height="20" rx="2" fill="none" stroke="#fff" stroke-width="2"/><path d="M1 6 Q4 3 5 6 L5 14 Q3 17 1 14 Z" fill="#fff"/></svg>
      555-014-2290
    </div>
    <div class="footer-links">
      <span><svg width="9" height="9"><circle cx="4.5" cy="4.5" r="4" fill="none" stroke="#fff" stroke-width="1.2"/></svg>info@dksireninstallers.com</span>
      <span><svg width="9" height="9"><circle cx="4.5" cy="4.5" r="4" fill="none" stroke="#fff" stroke-width="1.2"/><line x1=".5" y1="4.5" x2="8.5" y2="4.5" stroke="#fff"/></svg>www.dksireninstallers.com</span>
    </div>
  </div>
</section>

</body>
</html>
```